Kelvora trustee touch - styling

We have a prototyped single page application. The content is in place what we need is restyling to

- make it more user friendly
- modern look and feel
- improve accessibility features
- use our brand guidelines (screen shots attached of the full website)

Prototype is available at http://plinthdesk.examplehost.net/

Target form factor:
Primary - tablet
Secondary - desktop

Target Market(s)

Business users - not financial professionals but people working for big companies who have some limited training in the concepts

Number of Pages Required

1 page

Requirements
Must have
• Touch user interface

```html
<!DOCTYPE html>
<html lang="en">
<head>
<meta charset="utf-8">
<title>Kelvora – VaR</title>
<link rel="stylesheet" href="https://fonts.googleapis.com/css2?family=Signika:wght@300;400;600&family=Montserrat:wght@400;600&display=swap">
<style>
:root{
  --topbar:#1e2327;
  --brand:#0a64b8;
  --brand-text:#1f6cb0;
  --page:#f3f3f3;
  --card:#ffffff;
  --line:#e3e3e3;
  --ink:#2b2b2b;
  --muted:#777;
  --bar-blue:#5a8fb8;
  --bar-gray:#808080;
  --magenta:#a5006b;
  --footer:#3c3c3c;
  --tab:#f0f0f0;
}
*{box-sizing:border-box;margin:0;padding:0}
html,body{width:1200px;height:656px;overflow:hidden}
body{position:relative;background:var(--page);font-family:"Signika",sans-serif;color:var(--ink)}
.abs{position:absolute;white-space:nowrap}

.topbar{position:absolute;left:0;top:0;width:1200px;height:32px;background:var(--topbar);font-family:"Montserrat",sans-serif;font-size:8.5px;color:#b9bec2}
.topbar .abs{top:11px}
.masthead{position:absolute;left:0;top:32px;width:1200px;height:72px;background:var(--brand);border-top:1px solid #2d87d6}
.brand-name{left:128px;top:18px;font-family:"Signika",sans-serif;font-weight:600;font-size:27px;color:#fff;letter-spacing:-.5px}
.brand-rule{left:257px;top:22px;width:1px;height:26px;background:#6ea5da}
.tagline{left:274px;top:24px;font-size:15px;font-weight:300;color:#cfe2f5}
.mainnav{font-family:"Montserrat",sans-serif;font-weight:600;font-size:12px;color:#fff;top:29px}

.page-title{left:135px;top:122px;font-size:27px;font-weight:600}
.page-sub{left:136px;top:157px;font-size:10.5px;color:#666}

.card{position:absolute;background:var(--card);border:1px solid var(--line)}
.summary{left:127px;top:180px;width:949px;height:120px}
.date{left:138px;top:189px;font-size:15.5px;font-weight:600;color:var(--brand-text)}
.label-blue{font-size:11px;color:var(--brand-text)}
.small{font-size:9.5px}
.rule{position:absolute;left:128px;width:947px;height:1px;background:var(--line)}

.tabs{position:absolute;left:127px;top:326px;height:31px;display:flex}
.tab{height:31px;padding:0 16px;border:1px solid #dcdcdc;border-left:none;background:var(--tab);font-size:12.5px;color:#8a8a8a;line-height:30px}
.tab:first-child{border-left:1px solid #dcdcdc}
.tab.active{background:#fff;border-bottom-color:#fff;color:var(--brand-text)}
.panel{left:127px;top:356px;width:949px;height:231px}
.chart-title{top:373px;font-size:15px;color:#4a86b8}
.chart-title em{font-style:normal;color:var(--magenta)}
.unit{top:401px;font-size:9px}
.chart{position:absolute}
.chart text{font-family:"Signika",sans-serif;font-size:7.5px;fill:#444}

.footer{position:absolute;left:0;top:618px;width:1200px;height:38px;background:var(--footer);font-family:"Montserrat",sans-serif;font-weight:600;font-size:12px;color:#fff}
.footer .abs{top:12px}
</style>
</head>
<body>

<header class="topbar">
  <svg class="abs" style="left:124px;top:10px" width="12" height="10" viewBox="0 0 12 10"><path d="M6 0L0 5h2v5h3V7h2v3h3V5h2z" fill="#b9bec2"/></svg>
  <span class="abs" style="left:142px">HOME</span>
  <span class="abs" style="left:206px">ABOUT</span>
  <span class="abs" style="left:278px">CONTACT</span>
  <span class="abs" style="left:350px">FAQ's</span>
  <span class="abs" style="left:868px">ENGLISH</span>
  <span class="abs" style="left:910px;top:12px;width:10px;height:7px;background:#c8cdd3"></span>
  <svg class="abs" style="left:925px;top:14px" width="6" height="4"><path d="M0 0h6L3 4z" fill="#b9bec2"/></svg>
  <svg class="abs" style="left:975px;top:10px" width="8" height="10"><rect x="0" y="4" width="8" height="6" fill="#b9bec2"/><path d="M2 4V2.5a2 2 0 0 1 4 0V4" stroke="#b9bec2" fill="none"/></svg>
  <span class="abs" style="left:986px">LOGIN</span>
  <svg class="abs" style="left:1030px;top:10px" width="10" height="10"><circle cx="5" cy="3" r="2.6" fill="#b9bec2"/><path d="M0 10a5 4 0 0 1 10 0z" fill="#b9bec2"/></svg>
  <span class="abs" style="left:1044px">SIGNUP</span>
</header>

<nav class="masthead">
  <span class="abs brand-name">Kelvora</span>
  <span class="abs brand-rule"></span>
  <span class="abs tagline">Tag Line Place here</span>
  <svg class="abs" style="left:552px;top:31px" width="12" height="10"><rect x="1" y="1" width="10" height="7" fill="none" stroke="#fff" stroke-width="1.5"/><rect x="3" y="9" width="6" height="1" fill="#fff"/></svg>
  <span class="abs mainnav" style="left:570px">Dashboard</span>
  <svg class="abs" style="left:661px;top:31px" width="11" height="11"><circle cx="5.5" cy="5.5" r="5" fill="#fff"/><path d="M5.5 0.5v10M0.5 5.5h10" stroke="#0a64b8"/></svg>
  <span class="abs mainnav" style="left:675px">Analytics</span>
  <svg class="abs" style="left:731px;top:35px" width="8" height="5"><path d="M0 0h8L4 5z" fill="#fff"/></svg>
  <span class="abs mainnav" style="left:778px">Risk</span>
  <span class="abs mainnav" style="left:829px">ALM</span>
  <span class="abs mainnav" style="left:882px">Optimizer</span>
  <span class="abs mainnav" style="left:967px">urves</span>
  <svg class="abs" style="left:1027px;top:30px" width="10" height="11"><circle cx="5" cy="3" r="2.8" fill="#fff"/><path d="M0 11a5 4.5 0 0 1 10 0z" fill="#fff"/></svg>
  <span class="abs mainnav" style="left:1040px">Admin</span>
</nav>

<main>
  <h1 class="abs page-title">VaR</h1>
  <p class="abs page-sub">›&nbsp; Economic basis as at August 31 2014; 95% Var</p>

  <section class="card summary"></section>
  <span class="abs date">08/31/2014</span>
  <span class="abs label-blue" style="left:138px;top:218px">Scheme</span>
  <span class="abs small" style="left:138px;top:236px">ZYX Pension Scheme</span>
  <span class="abs label-blue" style="left:793px;top:219px;font-size:10.5px"><span style="display:inline-block;width:6px;height:6px;background:var(--bar-blue);margin-right:4px"></span>1yr Monte Carlo</span>
  <span class="abs small" style="left:946px;top:219px;font-size:10.5px">Net risk, GBP m</span>
  <span class="abs" style="left:755px;top:233px;width:128px;height:18px;background:var(--magenta);color:#fff;font-size:10.5px;text-align:right;padding:2px 5px 0 0">134,930,138</span>
  <span class="abs" style="left:907px;top:233px;width:154px;height:18px;background:var(--bar-blue)"></span>
  <span class="rule" style="top:251px"></span>
  <span class="abs small" style="left:138px;top:258px;color:#666">Diversification</span>
  <span class="abs" style="left:873px;top:256px;font-size:8px">0</span>
  <span class="rule" style="top:275px"></span>
  <span class="abs small" style="left:138px;top:282px;color:#666">Total</span>
  <span class="abs" style="left:819px;top:279px;font-size:10.5px">134,930,138</span>
  <svg class="abs" style="left:900px;top:274px" width="170" height="20" viewBox="900 274 170 20">
    <g stroke="#999"><path d="M909 276v3M937 276v3M968 276v3M994 276v3M1023 276v3M1052 276v3"/></g>
    <g font-family="Signika,sans-serif" font-size="8" fill="#333" text-anchor="middle">
      <text x="909" y="290">0</text><text x="937" y="290">25</text><text x="968" y="290">50</text><text x="994" y="290">75</text><text x="1023" y="290">100</text><text x="1052" y="290">125</text>
    </g>
  </svg>

  <section class="card panel"></section>
  <div class="tabs">
    <span class="tab active">Attribution</span>
    <span class="tab">Distribution</span>
    <span class="tab">Market Events</span>
    <span class="tab">Correlation</span>
    <span class="tab">What if ?</span>
    <span class="tab">Downloads</span>
  </div>
  <svg class="abs" style="left:1009px;top:335px" width="70" height="14">
    <path d="M3 1h4v5h3L5 10 0 6h3z M0 12h10v2H0z" fill="#3a9ad9"/>
    <g transform="translate(24 0)"><rect x="2" y="0" width="7" height="4" fill="#333"/><rect x="0" y="4" width="11" height="6" fill="#333"/><rect x="2" y="8" width="7" height="5" fill="#fff" stroke="#333"/></g>
    <path d="M49 2l8 8M57 2l-8 8" stroke="#c8102e" stroke-width="2.2"/>
  </svg>

  <h2 class="abs chart-title" style="left:145px">Risk attribution</h2>
  <span class="abs unit" style="left:145px">GBP m</span>
  <svg class="abs" style="left:566px;top:378px" width="10" height="10"><g fill="#999"><rect x="0" y="0" width="2" height="2"/><rect x="3" y="0" width="2" height="2"/><rect x="6" y="0" width="2" height="2"/><rect x="0" y="3" width="2" height="2"/><rect x="3" y="3" width="2" height="2"/><rect x="6" y="3" width="2" height="2"/><rect x="0" y="6" width="2" height="2"/><rect x="3" y="6" width="2" height="2"/><rect x="6" y="6" width="2" height="2"/></g></svg>
  <svg class="chart" style="left:140px;top:420px" width="440" height="160" viewBox="140 420 440 160">
    <g stroke="#e6e6e6"><path d="M160 428H577M160 447H577M160 466H577M160 486H577M160 505H577M160 525H577M160 545H577"/></g>
    <path d="M148 562H577" stroke="#ccc"/>
    <g text-anchor="end"><text x="157" y="431">350</text><text x="157" y="450">300</text><text x="157" y="469">250</text><text x="157" y="489">200</text><text x="157" y="508">150</text><text x="157" y="528">100</text><text x="157" y="548">50</text></g>
    <g fill="#5a8fb8">
      <rect x="176" y="512" width="16" height="50"/><rect x="222" y="462" width="16" height="50"/><rect x="269" y="453" width="16" height="9"/>
      <rect x="314" y="450" width="16" height="3"/><rect x="361" y="448" width="16" height="2"/><rect x="407" y="446" width="16" height="2.5"/><rect x="454" y="446" width="16" height="2.5"/>
    </g>
    <rect x="499" y="446" width="16" height="64" fill="#808080"/>
    <rect x="546" y="509" width="16" height="53" fill="#a5006b"/>
    <g stroke="#ddd"><path d="M206 562v13M252 562v13M298 562v13M345 562v13M391 562v13M437 562v13M483 562v13M530 562v13M577 562v13"/></g>
    <g text-anchor="middle"><text x="182" y="574">Interest rate</text><text x="229" y="574">Inflation</text><text x="275" y="574">Equity</text><text x="322" y="574">EX</text><text x="367" y="574">Credit</text><text x="414" y="574">Swap spread</text><text x="460" y="574">Property</text><text x="506" y="574">Diversification</text><text x="553" y="574">Net risk</text></g>
  </svg>

  <span class="abs" style="left:601px;top:368px;width:1px;height:206px;background:#d6d6d6"></span>

  <h2 class="abs chart-title" style="left:623px">Risk Breakdown - <em>Net risk</em></h2>
  <span class="abs unit" style="left:624px">GBP m</span>
  <svg class="abs" style="left:1045px;top:378px" width="10" height="10"><g fill="#999"><rect x="0" y="0" width="2" height="2"/><rect x="3" y="0" width="2" height="2"/><rect x="6" y="0" width="2" height="2"/><rect x="0" y="3" width="2" height="2"/><rect x="3" y="3" width="2" height="2"/><rect x="6" y="3" width="2" height="2"/><rect x="0" y="6" width="2" height="2"/><rect x="3" y="6" width="2" height="2"/><rect x="6" y="6" width="2" height="2"/></g></svg>
  <svg class="chart" style="left:618px;top:420px" width="442" height="160" viewBox="618 420 442 160">
    <g stroke="#e6e6e6"><path d="M640 428H1056M640 447H1056M640 466H1056M640 486H1056M640 505H1056M640 525H1056M640 545H1056"/></g>
    <path d="M628 562H1056" stroke="#ccc"/>
    <g text-anchor="end"><text x="636" y="431">350</text><text x="636" y="450">300</text><text x="636" y="469">250</text><text x="636" y="489">200</text><text x="636" y="508">150</text><text x="636" y="528">100</text><text x="636" y="548">50</text></g>
    <g fill="#5a8fb8">
      <rect x="661" y="472" width="16" height="90"/><rect x="720" y="451" width="16" height="21"/><rect x="780" y="438" width="16" height="13"/>
      <rect x="839" y="437.5" width="16" height="2.5"/><rect x="898" y="437.5" width="16" height="2.5"/>
    </g>
    <rect x="958" y="437.5" width="16" height="50.5" fill="#808080"/>
    <rect x="1018" y="488" width="16" height="74" fill="#a5006b"/>
    <g stroke="#ddd"><path d="M639 562v13M698 562v13M757 562v13M817 562v13M876 562v13M936 562v13M995 562v13M1055 562v13"/></g>
    <g text-anchor="middle"><text x="668" y="574">Liabilities</text><text x="727" y="574">Fixed Income</text><text x="787" y="574">Equity</text><text x="846" y="574">Property</text><text x="906" y="574">Cash</text><text x="966" y="574">Diversification</text><text x="1025" y="574">Net risk</text></g>
  </svg>
</main>

<footer class="footer">
  <span class="abs" style="left:122px">Home</span>
  <span class="abs" style="left:170px">/</span>
  <span class="abs" style="left:188px">About us</span>
  <span class="abs" style="left:252px">/</span>
  <span class="abs" style="left:270px">Privacy policy</span>
  <span class="abs" style="left:361px">/</span>
  <span class="abs" style="left:379px">Terms of service</span>
  <span class="abs" style="left:484px">/</span>
  <span class="abs" style="left:503px">News</span>
  <svg class="abs" style="left:938px;top:10px;top:10px" width="136" height="18" aria-label="Social links">
    <g fill="#e6e6e6"><circle cx="10" cy="9" r="7"/><circle cx="39" cy="9" r="7"/><circle cx="67" cy="9" r="7"/><circle cx="96" cy="9" r="7"/><circle cx="125" cy="9" r="7"/></g>
  </svg>
</footer>

</body>
</html>
```